Attractive WP design (Velmora) for our textile production and trading business

We need a design for our new website. We would like it to be based on the WP theme Velmora.

1) Description of the business
Kandrel GmbH is a textile company that is specialized in production and trading of high-quality cotton fabrics/products.

We…
• design and develop
• weave (incl. special weaving/embroidery technique)
• shear
• finish the products (Logo printing, packing)

Our products are…
• Swiss Ghutra
• Shemagh (=Yashmagh) (https://www.tervastoff.ch/en/competence/clothing-textiles/clothing-for-arab-and-african-markets/#210)
• Desdasha’s (https://www.tervastoff.ch/en/competence/clothing-textiles/clothing-for-arab-and-african-markets/#210)
• Emmas and Shawls
Emmas are traditional head coverings worn by Muslim man in Sudan. The cloth of exactly 5 yards in length is winded around the head like a turban. The cloth can be plain white, have a decorative trim or be colored. There are also matching scarfs.
• Brocade/Damask
• Atiku
• Kemora Voile (https://pomlatrade.com/products/kemora-3?_pos=2&_sid=98a067e86&_ss=r)
--> Please see attached pictures of the different fabrics and products

2) Target audience and users
• (Foreign) wholesalers interested in trading with Kandrel

3) Goals of the website
Kandrel has been a family-run textile business for 17 years with no web presence. The majority of our historical sales have been based on pre-existing relationships or word-of-mouth connections. Now, we seek to diversify our customer base. For this, we want our first website/online presence in order to:

• Enable foreign wholesalers to discover Kandrel as a supplier of Swiss quality fabric;
• Showcase both our current specific product line as well as our general manufacturing capabilities for new custom products;
• Enable inquiries/orders by interested parties

4) Design wishes
The design should reflect our high quality textiles. The design should be clean, inviting, friendly and professional. Colors can be chosen freely. Pictures should not overload sites but support our goal to attract and inspire future buyers.

If you have any questions, please reach out to us!

• the site will be multilingual (german/english/possibly french)

```html
<!DOCTYPE html>
<html lang="en">
<head>
<meta charset="utf-8">
<title>Kandrel GmbH</title>
<link href="https://fonts.googleapis.com/css2?family=Roboto:wght@400;500;700;900&display=swap" rel="stylesheet">
<style>
:root{
  --black:#000;
  --ink:#1e1e1e;
  --text:#333;
  --muted:#555;
  --light:#f5f5f5;
  --white:#fff;
  --line:#d8d8d8;
}
*{box-sizing:border-box;margin:0;padding:0}
html,body{width:1200px;height:3720px;overflow:hidden}
body{position:relative;font-family:"Roboto",sans-serif;color:var(--text);background:var(--white)}
.abs{position:absolute}
.center{text-align:center;left:0;width:1200px}

/* top bar */
.topbar{top:0;left:0;width:1200px;height:32px;background:var(--black);color:var(--white);font-size:13px}
.topbar span{position:absolute;top:8px;display:flex;align-items:center;gap:5px}
.social{position:absolute;top:9px;width:14px;height:14px;border-radius:50%;background:var(--white)}

/* header */
.logo-word{font-weight:700;font-size:34px;color:var(--black);display:flex;align-items:center;gap:8px}
.logo-word i{display:block;width:14px;height:14px;border-radius:50%;background:var(--black)}
.search{top:65px;left:361px;width:414px;height:48px;border:1px solid #bbb;border-radius:24px}
.search .ph{position:absolute;left:18px;top:16px;font-size:12px;color:#666}
.search .btn{position:absolute;right:3px;top:3px;width:142px;height:40px;border-radius:20px;background:var(--black);color:var(--white);font-weight:700;font-size:16px;text-align:center;line-height:40px}
.call{top:62px;left:858px}
.call small{position:absolute;left:56px;top:2px;font-size:14px;white-space:nowrap;color:#222}
.call strong{position:absolute;left:56px;top:22px;font-size:21px;white-space:nowrap;color:#111}
.nav{top:142px;left:102px;width:997px;height:50px;background:var(--black);z-index:2;display:flex;justify-content:center;gap:35px;align-items:center}
.nav a{color:var(--white);text-decoration:none;font-size:14px;font-weight:500}

/* hero */
.hero{top:166px;left:0;width:1200px;height:599px;background:linear-gradient(125deg,#6d2030 0%,#8a2b3a 30%,#7b6a70 55%,#9a9a9e 75%,#5d5d62 100%)}
.hero .veil{position:absolute;inset:0;background:rgba(40,40,45,.35)}
.hero-kicker{top:328px;font-size:25px;font-weight:500;color:var(--white)}
.hero-title{top:372px;font-size:48px;font-weight:700;line-height:60px;color:var(--white)}
.hero-sub{top:514px;font-size:14px;color:var(--white)}
.hero-btn{top:567px;left:517px;width:166px;height:46px;border-radius:23px;background:var(--black);color:var(--white);font-weight:700;font-size:16px;text-align:center;line-height:46px}
.arrow{width:64px;height:64px;border:2px solid var(--white);border-radius:50%;display:flex;align-items:center;justify-content:center}

/* sections */
.section-title{font-size:35px;font-weight:700;color:var(--black)}
.rule{height:4px;width:46px;background:var(--black)}
.lead{font-size:14.5px;line-height:30px;color:var(--text)}
.outline-btn{border:2px solid var(--black);border-radius:24px;font-size:16px;font-weight:500;color:var(--black);text-align:center}
.band-light{left:0;width:1200px;background:var(--light)}

.step{width:250px;text-align:center}
.step .icon{width:104px;height:104px;margin:0 auto;border-radius:50%;background:var(--white);box-shadow:0 2px 8px rgba(0,0,0,.08);display:flex;align-items:center;justify-content:center}
.step h3{margin-top:28px;font-size:17px;font-weight:500;color:var(--black)}
.step p{margin-top:4px;font-size:14.5px;line-height:30px}

.product{width:238px;text-align:center}
.product .photo{height:268px}
.product .tag{margin-top:20px;font-size:11px;font-weight:500;color:#222}
.product h4{margin-top:4px;font-size:20px;font-weight:500;color:#111}
.product .price{margin-top:6px;font-size:15px;color:#444}
.nav-dot{width:38px;height:38px;border-radius:50%;background:#555;display:flex;align-items:center;justify-content:center}

.badge{top:2797px;height:68px;background:var(--white);box-shadow:0 1px 6px rgba(0,0,0,.08);display:flex;align-items:center;justify-content:center}
.badge i{display:block;width:30px;height:30px;border-radius:50%;background:#8a8a8a}

.news{top:2950px;height:332px;left:0;width:1200px;background:var(--ink)}
.news-input{top:3149px;left:306px;width:438px;height:48px;border:2px solid var(--white);background:var(--white);font-size:12px;color:#333;padding:17px 10px}
.news-btn{top:3149px;left:744px;width:154px;height:48px;border:2px solid var(--white);background:var(--white);color:var(--black);font-weight:700;font-size:16px;text-align:center;line-height:44px}

.foot-col h5{font-size:19px;font-weight:500;color:#111;margin-bottom:14px}
.foot-col li{list-style:none;font-size:12.5px;line-height:30px;color:#333;padding-left:4px}
.select{top:3568px;left:836px;width:299px;height:42px;background:var(--white);box-shadow:0 1px 6px rgba(0,0,0,.15);font-size:12px;padding:14px 14px}
.card{top:3677px;width:32px;height:20px;border-radius:2px}
</style>
</head>
<body>

<!-- top bar -->
<div class="abs topbar">
  <span style="left:113px"><svg width="12" height="9" viewBox="0 0 12 9"><rect x="0.5" y="0.5" width="11" height="8" fill="none" stroke="#fff"/><path d="M0.5 0.5 6 5 11.5 0.5" fill="none" stroke="#fff"/></svg>info@kandrel-textil.ch</span>
  <span style="left:345px"><svg width="8" height="12" viewBox="0 0 8 12"><path d="M4 0a4 4 0 0 1 4 4c0 3-4 8-4 8S0 7 0 4a4 4 0 0 1 4-4z" fill="#fff"/></svg>Lindenweg 14 CH – 9000 Talbach Switzerland</span>
  <span style="left:904px">Eng ▾</span>
  <i class="social" style="left:960px"></i>
  <i class="social" style="left:993px"></i>
  <i class="social" style="left:1027px"></i>
  <i class="social" style="left:1062px"></i>
</div>

<!-- header -->
<div class="abs logo-word" style="top:66px;left:113px"><i></i>Kandrel</div>
<div class="abs search"><span class="ph">Enter The Here</span><span class="btn">SEARCH</span></div>
<div class="abs call">
  <svg width="46" height="46" viewBox="0 0 46 46"><circle cx="23" cy="23" r="21.5" fill="none" stroke="#111" stroke-width="2"/><path d="M16 14c2-1 3 0 4 3s0 3-1 4c1 3 3 5 6 6 1-1 2-2 4-1s4 2 3 4c-1 3-4 3-7 1-5-3-9-7-10-12 0-2 0-4 1-5z" fill="#111"/></svg>
  <small>Call Us Today</small>
  <strong>+41 71 000 12 34</strong>
</div>
<nav class="abs nav">
  <a href="#">HOME</a><a href="#">ABOUT US</a><a href="#">PRODUCTS</a><a href="#">TESTIMONIALS</a><a href="#">BLOGS</a><a href="#">CONTACT US</a>
</nav>

<!-- hero -->
<section class="abs hero" role="img" aria-label="Close-up photo of red and white checked cotton fabric folds"><div class="veil"></div></section>
<div class="abs center hero-kicker">KANDREL GMBH</div>
<h1 class="abs center hero-title">LOREM IPSUM DOLOR SIT AMET CONSEC<br>TETUR ADIPISCING ELIT SED DO</h1>
<p class="abs center hero-sub">Lorem ipsum dolor sit amet, consectetur adipiscing elit, sed do eiusmod tempor incididunt ut labore</p>
<div class="abs hero-btn">GET STARTED</div>
<div class="abs arrow" style="top:433px;left:40px"><svg width="12" height="18" viewBox="0 0 12 18"><path d="M10 1 2 9l8 8" fill="none" stroke="#fff" stroke-width="2"/></svg></div>
<div class="abs arrow" style="top:433px;left:1094px"><svg width="12" height="18" viewBox="0 0 12 18"><path d="M2 1l8 8-8 8" fill="none" stroke="#fff" stroke-width="2"/></svg></div>

<!-- about -->
<h2 class="abs section-title" style="top:846px;left:110px">ABOUT KANDREL GMBH</h2>
<div class="abs rule" style="top:896px;left:110px"></div>
<p class="abs lead" style="top:922px;left:110px;width:490px">Lorem ipsum dolor sit amet, consectetur adipiscing elit, sed do eiusmod tempor incididunt ut labore et dolore magna aliqua. Ut enim ad minim veni am, quis nostrud exercitation ullamco laboris nisi ut aliquip ex ea commo do consequat. Duis aute irure dolor in reprehenderit in voluptate velit esse cillum dolore eu fugiat nulla pariatur. Excepteur sint occaecat cupidatat non proident, sunt in culpa qui officia deserunt mollit anim id est laboru m.Lorem ipsum dolor sit amet, consectetur adipiscing elit, sed do eiusmod tempor incididunt ut labore et dolore magna aliqua. Ut enim ad minim veniam, quis nostrud exercitation.</p>
<div class="abs outline-btn" style="top:1213px;left:110px;width:177px;height:48px;line-height:44px">LEARN MORE</div>
<div class="abs" style="top:990px;left:624px;width:466px;text-align:center;font-size:96px;font-weight:700;color:var(--black)">Kandrel</div>

<!-- how it works -->
<section class="abs band-light" style="top:1347px;height:563px"></section>
<h2 class="abs center section-title" style="top:1423px">HOW ITS WORKS</h2>
<div class="abs rule" style="top:1474px;left:577px"></div>
<p class="abs center lead" style="top:1492px;padding:0 215px">Lorem ipsum dolor sit amet, consectetur adipiscing elit, sed do eiusmod tempor incididunt ut labore et dolore magna aliqua. Ut enim ad minim veniam quis nostrud exercitation.</p>
<div class="abs step" style="top:1590px;left:90px">
  <div class="icon"><svg width="50" height="50" viewBox="0 0 50 50" fill="none" stroke="#111" stroke-width="2"><rect x="10" y="26" width="30" height="18" rx="2"/><path d="M6 44h38M22 32l-3 3 3 3M28 32l3 3-3 3"/><circle cx="25" cy="14" r="7"/></svg></div>
  <h3>DESIGN AND DEVELOP</h3>
  <p>Lorem ipsum dolor sit amet, consectetur adipiscing elit, sed do eiusmod tempor incididunt.</p>
</div>
<div class="abs step" style="top:1590px;left:346px">
  <div class="icon"><svg width="50" height="50" viewBox="0 0 50 50" fill="none" stroke="#111" stroke-width="2"><circle cx="30" cy="20" r="11"/><circle cx="30" cy="20" r="3"/><path d="M8 30h36M12 30v14M40 30v14M8 12h8v18H8z"/></svg></div>
  <h3>WEAVE</h3>
  <p>Lorem ipsum dolor sit amet, consectetur adipiscing elit, sed do eiusmod tempor incididunt.</p>
</div>
<div class="abs step" style="top:1590px;left:603px">
  <div class="icon"><svg width="50" height="50" viewBox="0 0 50 50" fill="none" stroke="#111" stroke-width="2"><path d="M16 6l12 22M34 6 22 28"/><circle cx="19" cy="36" r="6"/><circle cx="31" cy="36" r="6"/></svg></div>
  <h3>SHEAR</h3>
  <p>Lorem ipsum dolor sit amet, consectetur adipiscing elit, sed do eiusmod tempor incididunt.</p>
</div>
<div class="abs step" style="top:1590px;left:858px">
  <div class="icon"><svg width="50" height="50" viewBox="0 0 50 50" fill="none" stroke="#111" stroke-width="2"><path d="M18 8h14l8 6v30H10V14z"/><path d="M25 12v32M18 8l7 8 7-8"/></svg></div>
  <h3>FINISH THE PRODUCTS</h3>
  <p>Lorem ipsum dolor sit amet, consectetur adipiscing elit, sed do eiusmod tempor incididunt.</p>
</div>

<!-- products -->
<h2 class="abs center section-title" style="top:1987px">OUR PRODUCTS</h2>
<div class="abs rule" style="top:2038px;left:577px"></div>
<p class="abs center lead" style="top:2054px;padding:0 215px">Lorem ipsum dolor sit amet, consectetur adipiscing elit, sed do eiusmod tempor incididunt ut labore et dolore magna aliqua. Ut enim ad minim veniam quis nostrud exercitation.</p>
<div class="abs product" style="top:2141px;left:111px">
  <div class="photo" role="img" aria-label="Photo of folded white ghutra cloth" style="background:linear-gradient(160deg,#d8d8d8,#8d8d8d 60%,#2a2a2a)"></div>
  <div class="tag">LOREM IPSUM DOLOR</div><h4>SWISS GHUTRA</h4><div class="price">$ 190:00</div>
</div>
<div class="abs product" style="top:2141px;left:358px">
  <div class="photo" role="img" aria-label="Photo of a white traditional robe garment" style="background:linear-gradient(180deg,#f2f2f2,#e2e2e2)"></div>
  <div class="tag">LOREM IPSUM DOLOR</div><h4>SHEMAGH</h4><div class="price">$ 190:00</div>
</div>
<div class="abs product" style="top:2141px;left:605px">
  <div class="photo" role="img" aria-label="Photo of black and white woven textile" style="background:linear-gradient(135deg,#6a6a6a,#3a3a3a)"></div>
  <div class="tag">LOREM IPSUM DOLOR</div><h4>DESDASHA’S</h4><div class="price">$ 190:00</div>
</div>
<div class="abs product" style="top:2141px;left:852px">
  <div class="photo" role="img" aria-label="Photo of a blue knitted shawl" style="background:linear-gradient(90deg,#efefef 30%,#4aa3e0 45%,#4aa3e0 55%,#efefef 70%)"></div>
  <div class="tag">LOREM IPSUM DOLOR</div><h4>EMMAS AND SHAWLS</h4><div class="price">$ 190:00</div>
</div>
<div class="abs nav-dot" style="top:2190px;left:92px"><svg width="8" height="12" viewBox="0 0 8 12"><path d="M6 1 1 6l5 5" fill="none" stroke="#fff" stroke-width="2"/></svg></div>
<div class="abs nav-dot" style="top:2190px;left:1070px"><svg width="8" height="12" viewBox="0 0 8 12"><path d="M2 1l5 5-5 5" fill="none" stroke="#fff" stroke-width="2"/></svg></div>

<!-- partners -->
<section class="abs band-light" style="top:2578px;height:372px"></section>
<h2 class="abs center section-title" style="top:2654px">OUR PARTNER LOGO</h2>
<div class="abs rule" style="top:2705px;left:577px"></div>
<p class="abs center lead" style="top:2720px;padding:0 215px">Lorem ipsum dolor sit amet, consectetur adipiscing elit, sed do eiusmod tempor incididunt ut labore et dolore magna aliqua. Ut enim ad minim veniam quis nostrud exercitation.</p>
<div class="abs badge" style="left:110px;width:150px"><i></i></div>
<div class="abs badge" style="left:276px;width:150px"><i></i></div>
<div class="abs badge" style="left:440px;width:151px"><i></i></div>
<div class="abs badge" style="left:606px;width:151px"><i></i></div>
<div class="abs badge" style="left:773px;width:148px"><i></i></div>
<div class="abs badge" style="left:937px;width:150px"><i></i></div>

<!-- newsletter -->
<section class="abs news"></section>
<h2 class="abs center section-title" style="top:3025px;color:var(--white)">SUBSCRIBE OUR NEWSLETTER</h2>
<p class="abs center lead" style="top:3073px;padding:0 160px;color:var(--white);font-size:15px">Lorem ipsum dolor sit amet, consectetur adipiscing elit, sed do eiusmod tempor incididunt ut labore et dolore magna aliqua. Quis ipsum suspendisse ultrices gravida. Risus commodo viverra maecenas accumsan lacus vel facilisis.</p>
<div class="abs news-input">Enter the Email</div>
<div class="abs news-btn">SUBSCRIBE</div>

<!-- footer -->
<div class="abs foot-col" style="top:3346px;left:62px"><h5>CATEGORIES</h5><ul><li>Swiss Ghutra</li><li>Shemagh</li><li>Desdasha’s</li><li>Emmas and Shawls</li><li>Brocade/Damask</li><li>Atiku</li><li>Kemora Voile</li></ul></div>
<div class="abs foot-col" style="top:3346px;left:332px"><h5>INFORMATION</h5><ul><li>Home</li><li>About Us</li><li>Products</li><li>Testimonials</li><li>Blogs</li><li>Contact Us</li></ul></div>
<div class="abs foot-col" style="top:3346px;left:582px"><h5>CUSTOMER SERVICE</h5><ul><li>Search Terms</li><li>Advanced Search</li><li>Orders and Returns</li><li>Contact Us</li><li>Gift Certificates</li><li>Consultant</li><li>Store Locations</li></ul></div>
<div class="abs foot-col" style="top:3346px;left:897px"><h5>STORE INFO</h5><ul><li>Kandrel GmbH Telefon Lindenweg 14</li><li>CH – 9000 Talbach Switzerland</li><li>Telefon+41 71 000 12 34</li><li>E-Mail: info@kandrel-textil.ch</li><li>CHE-000.123.456 MWST</li></ul></div>
<div class="abs select">USD<span style="position:absolute;right:14px;top:12px">▾</span></div>
<div class="abs" style="top:3658px;left:14px;width:1170px;height:1px;background:var(--line)"></div>
<div class="abs card" style="left:53px;background:#333"></div>
<div class="abs card" style="left:94px;background:#1a3f8f"></div>
<div class="abs card" style="left:132px;background:#2b7fd0"></div>
<div class="abs card" style="left:160px;background:#e7e7e7"></div>
<div class="abs card" style="left:196px;background:#dfe7f2"></div>
<div class="abs card" style="left:230px;background:#eee"></div>
<div class="abs" style="top:3671px;left:540px;width:120px;text-align:center;font-weight:700;font-size:22px;color:var(--black)">Kandrel</div>
<div class="abs" style="top:3678px;left:800px;width:308px;text-align:right;font-size:12px;color:#333">© 2021 Kandrel GmbH. All Rights Reserved.</div>
<div class="abs" style="top:3688px;left:1158px;font-size:11px;color:#333">C 43</div>

</body>
</html>
```